New Business Cards for MB&LR

We need updated business cards for a staff of 15 engineers, estimators, project managers, and sales people. We have recently begun changes to our website and marketing material to improve our look and branding. We are an established fabricator specializing in pressure vessels, tanks, and structural steel. The owners require us to use the existing logo and old english text design. Also, we prefer dark grey or mostly black cards.
Target Market(s)
Engineers, purchasing agents, estimators, and project managers of; mining companies, refineries, industrial construction professionals
Industry/Entity Type
Business
Contact Information for Business Card
Logo, phone, website, email, etc.
Look and feel

```html
<!DOCTYPE html>
<html lang="en">
<head>
<meta charset="utf-8">
<title>MB&amp;LR Business Card</title>
<link rel="stylesheet" href="https://fonts.googleapis.com/css2?family=Open+Sans:wght@400;600;700&display=swap">
<style>
  :root {
    --backdrop: #e4e2de;
    --card-light: #f1f1f1;
    --card-dark: #1b1a1c;
    --ink-dark: #1b1a1c;
    --ink-light: #ffffff;
  }
  * { margin: 0; padding: 0; box-sizing: border-box; }
  html, body {
    width: 1200px; height: 960px; overflow: hidden;
    background: var(--backdrop);
    font-family: "Open Sans", Arial, sans-serif;
  }
  .card {
    position: absolute;
    width: 600px; height: 344px;
    box-shadow: 0 3px 8px rgba(0,0,0,0.35);
    overflow: hidden;
  }
  .card-front { left: 314px; top: 113px; background: var(--card-light); }
  .card-back { left: 312px; top: 472px; background: var(--card-dark); }
  .front-panel { position: absolute; inset: 0; }
  .brand {
    position: absolute;
    display: flex; align-items: center; gap: 8px;
    font-weight: 600; white-space: nowrap;
  }
  .brand-mark { width: 12px; height: 12px; }
  .card-front .brand {
    left: 164px; top: 130px; transform: translateX(-50%);
    font-size: 15px; color: var(--ink-dark);
  }
  .card-front .brand-mark { background: var(--ink-dark); }
  .contact {
    position: absolute; right: 31px; top: 156px;
    text-align: right; color: var(--ink-light);
  }
  .contact-name { font-size: 16px; font-weight: 700; line-height: 22px; }
  .contact-title { font-size: 15px; line-height: 22px; margin-bottom: 10px; }
  .contact-address { font-size: 14px; line-height: 20px; margin-bottom: 6px; }
  .contact-line {
    display: flex; justify-content: flex-end; align-items: center; gap: 7px;
    font-size: 14px; line-height: 20px;
  }
  .contact-line svg { width: 11px; height: 11px; fill: var(--ink-light); }
  .card-back .brand {
    left: 50%; top: 226px; transform: translateX(-50%);
    font-size: 19px; color: var(--ink-light);
  }
  .card-back .brand-mark { background: var(--ink-light); width: 14px; height: 14px; }
  .back-url {
    position: absolute; left: 0; right: 0; top: 262px;
    text-align: center; color: var(--ink-light);
    font-size: 14px; letter-spacing: 6px;
  }
</style>
</head>
<body>
  <section class="card card-front">
    <svg class="front-panel" width="600" height="344" viewBox="0 0 600 344" aria-hidden="true">
      <polygon points="448,0 600,0 600,344 258,344" fill="var(--card-dark)"/>
      <line x1="437" y1="0" x2="247" y2="344" stroke="var(--card-dark)" stroke-width="3"/>
      <line x1="427" y1="0" x2="237" y2="344" stroke="var(--card-dark)" stroke-width="3"/>
    </svg>
    <div class="brand"><span class="brand-mark"></span>Metal Beam &amp; Load Rigging</div>
    <div class="contact">
      <div class="contact-name">DANIEL REED</div>
      <div class="contact-title">CEO/FOUNDER</div>
      <div class="contact-address">48 East 300 South<br>Granite Falls 84120</div>
      <div class="contact-line">555.310.2741
        <svg viewBox="0 0 12 12" aria-label="phone"><path d="M1 4c0-2 2-3 5-3s5 1 5 3l-2 1-1-2H4L3 5zM3 6h6l1 5H2z"/></svg>
      </div>
      <div class="contact-line">555.310.2742
        <svg viewBox="0 0 12 12" aria-label="fax"><path d="M3 1h6v3H3zM1 5h10v5H9V8H3v2H1zM4 9h4v2H4z"/></svg>
      </div>
      <div class="contact-line">www.mbandlr.com
        <svg viewBox="0 0 12 12" aria-label="web"><circle cx="6" cy="6" r="5.5"/></svg>
      </div>
    </div>
  </section>

  <section class="card card-back">
    <div class="brand"><span class="brand-mark"></span>Metal Beam &amp; Load Rigging</div>
    <div class="back-url">www.mbandlr.com</div>
  </section>
</body>
</html>
```